Great Opportunity !! Masters in Business Analytics College Course

the size is Full Page, with bleed*
8”x 10.75" plus 0.25" bleed.
please leave one inch for footer
the purpose is attract students to join this college program .
this is for students in USA .
college age of around 24 years old
I am looking for a flyer that is unique and shows creativity .
A flyer that people would want to look at it because it is unique.
you can choose either vector, text ,or picture.
if you do picture it should be a white USA citizen wearing a white solid shirt and not long hair

Target Market(s)

USA students about 23 in age to join this college program

Industry/Entity Type

education

Colors
0054AA
0677BA
7BADD7
CADEEF
E8F1F8
0094D4
00A9DD
6FCCEA
C7EBF8
E9F6FB

Requirements
Must have
• the text should not be crowded .. .. .. the ad should not be full of text
Should not have
• not have very large text .. it should not be a flyer that is full of text .. you have to figure out how to avoid looking at the ad and it is very busy with text

```html
<!DOCTYPE html>
<html lang="en">
<head>
<meta charset="utf-8">
<title>Masters in Business Analytics – Open House Flyer</title>
<link rel="stylesheet" href="https://fonts.googleapis.com/css2?family=Bebas+Neue&family=Poppins:wght@400;500;600;700;800&display=swap">
<style>
  :root{
    --stage:#e9f6fb;
    --navy-deep:#032a5c;
    --navy:#0054aa;
    --blue:#0677ba;
    --sky:#0094d4;
    --cyan:#00a9dd;
    --aqua:#6fccea;
    --mist:#c7ebf8;
    --pale:#e8f1f8;
    --white:#ffffff;
    --rule:rgba(199,235,248,.45);
  }
  *{margin:0;padding:0;box-sizing:border-box}
  html,body{width:1200px;height:1200px;overflow:hidden;background:var(--stage)}
  body{position:relative;font-family:'Poppins',sans-serif;color:var(--white)}
  .flyer{
    position:absolute;left:146px;top:0;width:1312px;height:1736px;
    transform:scale(0.6912);transform-origin:0 0;background:var(--white);overflow:hidden;
  }
  .hero{position:absolute;left:0;top:0;width:1312px;height:1543px;overflow:hidden;
    background:radial-gradient(ellipse at 35% 35%,var(--blue) 0%,var(--navy) 45%,var(--navy-deep) 100%)}
  .footer-space{position:absolute;left:0;top:1543px;width:1312px;height:193px;background:var(--white)}
  .chart-bg,.beam{position:absolute;left:0;top:0}
  .portrait{position:absolute;left:645px;top:213px;width:590px;height:1320px;
    border-radius:260px 260px 40px 40px;
    background:linear-gradient(180deg,#4a3c33 0%,#eef2f5 22%,#f4f6f8 45%,#c8ad86 60%,#b79c74 78%,#2c2a2c 100%);opacity:.92}
  .abs{position:absolute;white-space:nowrap;line-height:1}
  .headline{left:88px;top:80px;font-weight:800;font-size:53px;line-height:59px;letter-spacing:.3px}
  .headline .light{font-weight:400}
  .headline .accent{color:var(--aqua)}
  .dots{left:88px;top:218px;display:flex;gap:6px}
  .dots i{width:12px;height:12px;border-radius:50%;background:var(--aqua);display:block}
  .dots i:nth-child(4){opacity:.7}.dots i:nth-child(5){opacity:.4}
  .kicker{left:88px;top:244px;font-size:50px;font-weight:400;letter-spacing:1px}
  .program{left:86px;top:298px;font-family:'Bebas Neue',sans-serif;font-size:84px;color:var(--aqua)}
  .school{left:88px;top:370px;font-size:36px;font-weight:700;letter-spacing:1.5px}
  .rule{position:absolute;left:88px;height:0;border-top:2px dashed var(--rule)}
  .pill{left:88px;top:471px;width:612px;height:112px;background:var(--mist);border-radius:16px;
    color:var(--navy);font-weight:700;font-size:33px;line-height:39px;padding:17px 0 0 36px}
  .salary-label{left:88px;top:614px;font-size:34px;font-weight:700;line-height:36px}
  .salary{left:288px;top:612px;font-family:'Bebas Neue',sans-serif;font-size:130px;color:var(--aqua)}
  .source{left:88px;top:740px;font-size:25px;letter-spacing:3px;color:var(--pale)}
  .list{font-size:21px;font-weight:500;display:flex;align-items:center;gap:8px}
  .list svg{width:12px;height:12px}
  .section{font-size:26px;font-weight:600;color:var(--aqua)}
  .open{left:88px;top:1084px;font-size:29px;font-weight:700;color:var(--aqua)}
  .day{left:86px;top:1126px;font-size:70px;font-weight:800;color:var(--aqua)}
  .month{left:178px;top:1128px;font-size:40px;font-weight:500}
  .weekday{left:178px;top:1164px;font-size:25px}
  .time{left:335px;top:1133px;width:192px;height:56px;background:var(--mist);border-radius:12px;
    color:var(--navy);font-size:35px;line-height:56px;text-align:center}
  .email{left:88px;top:1200px;font-size:29px;display:flex;align-items:center;gap:14px}
  .note{left:88px;top:1302px;font-size:27px;font-weight:600;color:var(--aqua)}
  .ribbon{position:absolute;left:82px;top:1338px}
  .ribbon-text{left:102px;top:1366px;font-family:'Bebas Neue',sans-serif;font-size:58px;color:var(--white)}
  .ribbon-text span{color:var(--mist)}
  .accred{left:263px;top:1362px;font-size:20px;font-weight:600;line-height:23px}
  .format{left:190px;top:1440px;font-size:18px;line-height:21px;color:var(--pale)}
  .format b{font-weight:700;color:var(--white)}
</style>
</head>
<body>
<div class="flyer">
  <section class="hero">
    <svg class="chart-bg" width="1312" height="1543" viewBox="0 0 1312 1543" aria-hidden="true">
      <g fill="#c7ebf8" opacity=".07">
        <rect x="10" y="1180" width="22" height="180"/><rect x="40" y="1120" width="22" height="240"/>
        <rect x="70" y="1200" width="22" height="160"/><rect x="560" y="1090" width="22" height="270"/>
        <rect x="590" y="1140" width="22" height="220"/><rect x="620" y="1060" width="22" height="300"/>
        <rect x="1240" y="1180" width="22" height="180"/><rect x="1270" y="1120" width="22" height="240"/>
        <rect x="950" y="230" width="30" height="190"/><rect x="1000" y="280" width="30" height="140"/>
        <rect x="1060" y="180" width="30" height="240"/>
      </g>
      <g fill="none" stroke="#c7ebf8" opacity=".1" stroke-width="1">
        <line x1="0" y1="1380" x2="1312" y2="1380"/><line x1="0" y1="1420" x2="1312" y2="1420"/>
        <line x1="0" y1="1470" x2="1312" y2="1470"/><line x1="0" y1="1530" x2="1312" y2="1530"/>
        <polyline points="0,1030 200,980 420,1010 640,900 900,960 1100,900 1312,880"/>
        <polyline points="560,470 650,320 760,410 860,300"/>
      </g>
    </svg>
    <svg class="beam" width="1312" height="1543" viewBox="0 0 1312 1543" aria-hidden="true">
      <defs>
        <linearGradient id="beamFade" x1="1" y1="0" x2="0" y2="1">
          <stop offset="0" stop-color="#e9f6fb" stop-opacity=".95"/>
          <stop offset=".55" stop-color="#c7ebf8" stop-opacity=".5"/>
          <stop offset="1" stop-color="#c7ebf8" stop-opacity="0"/>
        </linearGradient>
      </defs>
      <polygon points="1312,0 1306,0 720,1543 1130,1543 1312,780" fill="url(#beamFade)"/>
    </svg>
    <div class="portrait" role="img" aria-label="Photo of a young man with short hair in a white shirt and khaki trousers, sitting on a tall wooden chair"></div>

    <h1 class="abs headline">DO YOU HAVE AN ANALYTICAL MIND <span class="light">AND</span><br><span class="accent">SEEKING A PROFITABLE CAREER?</span></h1>
    <div class="abs dots"><i></i><i></i><i></i><i></i><i></i></div>
    <p class="abs kicker">A MASTERS IN</p>
    <h2 class="abs program">BUSINESS ANALYTICS</h2>
    <p class="abs school">HARLOW STATE COLLEGE**</p>
    <div class="rule" style="top:433px;width:672px"></div>

    <p class="abs pill">Can prepare you for some of<br>the most in-demand jobs.</p>
    <p class="abs salary-label">Jobs with<br>a median<br>salary of</p>
    <p class="abs salary">$100K+</p>
    <p class="abs source">(National Labor Outlook 2023)</p>
    <div class="rule" style="top:806px;width:580px"></div>

    <p class="abs list" style="left:88px;top:848px"><svg viewBox="0 0 12 12"><circle cx="6" cy="6" r="6" fill="#6fccea"/><path d="M3 6l2 2 4-4" stroke="#0054aa" stroke-width="1.6" fill="none"/></svg>BI Developer</p>
    <p class="abs list" style="left:315px;top:848px"><svg viewBox="0 0 12 12"><circle cx="6" cy="6" r="6" fill="#6fccea"/><path d="M3 6l2 2 4-4" stroke="#0054aa" stroke-width="1.6" fill="none"/></svg>Data Scientist</p>
    <p class="abs list" style="left:88px;top:881px"><svg viewBox="0 0 12 12"><circle cx="6" cy="6" r="6" fill="#6fccea"/><path d="M3 6l2 2 4-4" stroke="#0054aa" stroke-width="1.6" fill="none"/></svg>Data Analyst</p>
    <p class="abs list" style="left:315px;top:881px"><svg viewBox="0 0 12 12"><circle cx="6" cy="6" r="6" fill="#6fccea"/><path d="M3 6l2 2 4-4" stroke="#0054aa" stroke-width="1.6" fill="none"/></svg>Data Developer</p>

    <p class="abs section" style="left:88px;top:920px">Graduates were hired at</p>
    <p class="abs list" style="left:88px;top:960px"><svg viewBox="0 0 12 12"><circle cx="6" cy="6" r="6" fill="#6fccea"/><path d="M3 6l2 2 4-4" stroke="#0054aa" stroke-width="1.6" fill="none"/></svg>Verant</p>
    <p class="abs list" style="left:315px;top:960px"><svg viewBox="0 0 12 12"><circle cx="6" cy="6" r="6" fill="#6fccea"/><path d="M3 6l2 2 4-4" stroke="#0054aa" stroke-width="1.6" fill="none"/></svg>Corelink</p>
    <p class="abs list" style="left:462px;top:960px"><svg viewBox="0 0 12 12"><circle cx="6" cy="6" r="6" fill="#6fccea"/><path d="M3 6l2 2 4-4" stroke="#0054aa" stroke-width="1.6" fill="none"/></svg>Stanmore Life</p>
    <p class="abs list" style="left:88px;top:997px"><svg viewBox="0 0 12 12"><circle cx="6" cy="6" r="6" fill="#6fccea"/><path d="M3 6l2 2 4-4" stroke="#0054aa" stroke-width="1.6" fill="none"/></svg>Brayfield</p>
    <p class="abs list" style="left:315px;top:997px"><svg viewBox="0 0 12 12"><circle cx="6" cy="6" r="6" fill="#6fccea"/><path d="M3 6l2 2 4-4" stroke="#0054aa" stroke-width="1.6" fill="none"/></svg>Voltaro</p>
    <div class="rule" style="top:1056px;width:600px"></div>

    <p class="abs open">OPEN HOUSE</p>
    <p class="abs day">20</p>
    <p class="abs month">APRIL</p>
    <p class="abs weekday">Wednesday</p>
    <p class="abs time">7:30 pm.</p>
    <p class="abs email"><svg width="24" height="18" viewBox="0 0 24 18" aria-hidden="true"><rect x="1" y="1" width="22" height="16" fill="#6fccea"/><path d="M1 1l11 9 11-9" stroke="#0054aa" stroke-width="1.6" fill="none"/></svg>info@harlowstate.edu</p>
    <div class="rule" style="top:1270px;width:478px"></div>

    <p class="abs note">** Harlow State College</p>
    <svg class="ribbon" width="180" height="140" viewBox="0 0 180 140" aria-hidden="true">
      <polygon points="10,100 90,100 82,140" fill="#032a5c"/>
      <polygon points="0,0 170,12 166,96 4,84" fill="#0094d4"/>
      <polygon points="4,84 166,96 90,104 8,100" fill="#0677ba"/>
    </svg>
    <p class="abs ribbon-text">ONLY <span>5%</span></p>
    <p class="abs accred">of universities achieve<br>prestigious ABEA<br>accreditation.</p>
    <p class="abs format"><b>21 months</b> Hybrid with one weekly<br>in-person evening meeting</p>
  </section>
  <div class="footer-space"></div>
</div>
</body>
</html>
```